VOIP company busioness card redesign

Redesign business card to match our new logo and marketing material. Should include logo on one side and contact information on other side.

We like modern and clean

Industry/Entity Type

Phone Company

Contact Information for Business Card

One side should be logo other side should include contact info
Name
Phone Number
email
website

Other font styles liked:
• dont care

Requirements
Must have
• Modern sleek design that works with our logo

```html
<!DOCTYPE html>
<html lang="en">
<head>
<meta charset="utf-8">
<title>Veltrix Solutions – Business Card</title>
<link rel="stylesheet" href="https://fonts.googleapis.com/css2?family=Questrial&display=swap">
<style>
  :root {
    --bg: #2a2420;
    --card: #151515;
    --card-edge: #1d1d1d;
    --brand-blue: #1fa3e6;
    --brand-green: #8cc63f;
    --text-light: #d8d8d8;
    --text-muted: #9a9a9a;
  }
  html, body {
    margin: 0;
    padding: 0;
    width: 1200px;
    height: 716px;
    overflow: hidden;
    background: var(--bg);
    font-family: "Questrial", "Century Gothic", sans-serif;
  }
  .canvas {
    position: relative;
    width: 1200px;
    height: 716px;
  }
  .card {
    position: absolute;
    top: 203px;
    width: 540px;
    height: 310px;
    background: linear-gradient(160deg, #1c1c1c 0%, var(--card) 60%, #101010 100%);
    border: 1px solid var(--card-edge);
    border-radius: 6px;
    box-shadow: 0 18px 40px rgba(0,0,0,0.55);
  }
  .card--front { left: 40px; }
  .card--back  { left: 620px; }

  .brand {
    position: absolute;
    display: flex;
    flex-direction: column;
    align-items: flex-start;
  }
  .card--front .brand { left: 50%; top: 50%; transform: translate(-50%, -50%); }
  .card--back .brand  { left: 40px; top: 100px; }

  .brand__row { display: flex; align-items: flex-end; gap: 6px; }
  .brand__name {
    font-size: 50px;
    line-height: 1;
    color: var(--brand-blue);
    letter-spacing: -1px;
  }
  .card--back .brand__name { font-size: 42px; }
  .brand__suffix {
    font-size: 11px;
    color: var(--brand-green);
    padding-bottom: 6px;
    letter-spacing: 0.5px;
  }
  .brand__tagline {
    margin-top: 6px;
    font-size: 11px;
    color: var(--text-muted);
    letter-spacing: 0.3px;
  }

  .contact {
    position: absolute;
    left: 300px;
    top: 150px;
    color: var(--text-light);
  }
  .contact__name { font-size: 24px; letter-spacing: 0.5px; margin: 0; }
  .contact__title { font-size: 13px; color: var(--brand-blue); margin: 2px 0 16px; }
  .contact__list { list-style: none; margin: 0; padding: 0; }
  .contact__item {
    display: flex;
    align-items: center;
    gap: 10px;
    font-size: 14px;
    margin-bottom: 9px;
  }
  .contact__icon { width: 13px; height: 13px; fill: none; stroke: var(--brand-blue); stroke-width: 1.6; }
</style>
</head>
<body>
<main class="canvas">
  <section class="card card--front" aria-label="Card front">
    <div class="brand">
      <div class="brand__row">
        <span class="brand__name">Veltrix</span>
        <span class="brand__suffix">Solutions</span>
      </div>
      <span class="brand__tagline">Cloud Communications Redefined</span>
    </div>
  </section>

  <section class="card card--back" aria-label="Card back">
    <div class="brand">
      <div class="brand__row">
        <span class="brand__name">Veltrix</span>
        <span class="brand__suffix">Solutions</span>
      </div>
      <span class="brand__tagline">Cloud Communications Redefined</span>
    </div>

    <div class="contact">
      <p class="contact__name">Joe Smith</p>
      <p class="contact__title">Job Title</p>
      <ul class="contact__list">
        <li class="contact__item">
          <svg class="contact__icon" viewBox="0 0 14 14"><path d="M3 1.5l2.5 2.5-1.5 2a8 8 0 0 0 4 4l2-1.5 2.5 2.5-2 2C6 12.5 1.5 8 1.5 3.5z"/></svg>
          000 000 0000
        </li>
        <li class="contact__item">
          <svg class="contact__icon" viewBox="0 0 14 14"><rect x="1" y="3" width="12" height="8"/><path d="M1 3l6 5 6-5"/></svg>
          Email@xyz.com
        </li>
        <li class="contact__item">
          <svg class="contact__icon" viewBox="0 0 14 14"><circle cx="7" cy="7" r="5.5"/><path d="M1.5 7h11M7 1.5c-2.5 3-2.5 8 0 11M7 1.5c2.5 3 2.5 8 0 11"/></svg>
          www.yourwebsite.com
        </li>
      </ul>
    </div>
  </section>
</main>
</body>
</html>
```